Bright Ledger Path LLC Seminar Workbook Template

Our mission: Our mission is to provide students with amazing accounting literacy experiences in amazing learning environments so they can accomplish amazing career and business goals.
We would like to have a Microsoft Word template that we can use for all of our course content. We are profession; yet not stuffy. We teach a timeless subject; yet we are very modern.
Our logo is attached. We would like our logo or parts of our logo to be incorporated into the template (for example, perhaps the tagline is included in the bottom right corner). We have also attached a sample of a company's work. We do not like their design; but it's the kind of end product that we are interested in.
We are grateful for anyone who is interested in this project. Thank you for your help.

```html
<!DOCTYPE html>
<html lang="en">
<head>
<meta charset="utf-8">
<title>Bright Ledger Path LLC — Workbook Page</title>
<link href="https://fonts.googleapis.com/css2?family=Arimo:wght@400;700&display=swap" rel="stylesheet">
<style>
  :root {
    --lime: #a6bd0b;
    --teal: #05a3c9;
    --body-grey: #ababab;
    --paper: #ffffff;
  }
  html, body {
    margin: 0;
    padding: 0;
    width: 847px;
    height: 1200px;
    overflow: hidden;
    background: var(--paper);
  }
  .page {
    position: relative;
    width: 847px;
    height: 1200px;
    background: var(--paper);
    font-family: "Arimo", Arial, sans-serif;
    overflow: hidden;
  }
  .header-wave {
    position: absolute;
    top: 0;
    left: 0;
  }
  .brand-mark {
    position: absolute;
    left: 108px;
    top: 50px;
    margin: 0;
    font-size: 44px;
    font-weight: 400;
    letter-spacing: 2px;
    color: var(--teal);
    line-height: 1;
  }
  .content {
    position: absolute;
    left: 121px;
    width: 604px;
  }
  .content-title {
    position: absolute;
    top: 219px;
    margin: 0;
    font-size: 21px;
    font-weight: 700;
    color: var(--lime);
    white-space: nowrap;
  }
  .content-body {
    top: 285px;
  }
  .content-body p {
    margin: 0 0 12px;
    font-size: 18.5px;
    line-height: 34.5px;
    color: var(--body-grey);
    text-align: justify;
  }
  .content-body p.spaced {
    margin-top: 58px;
  }
  .footer-bars {
    position: absolute;
    left: 0;
    top: 1068px;
  }
  .footer-name {
    position: absolute;
    left: 59px;
    top: 1124px;
    margin: 0;
    font-size: 30px;
    font-weight: 400;
    color: var(--lime);
    white-space: nowrap;
  }
  .page-number {
    position: absolute;
    right: 0;
    top: 1133px;
    width: 65px;
    height: 41px;
  }
  .page-number::before {
    content: "";
    position: absolute;
    left: -6px;
    right: 0;
    top: 4px;
    height: 33px;
    background: var(--lime);
  }
  .page-number span {
    position: absolute;
    left: 0;
    top: 0;
    width: 40px;
    height: 41px;
    background: var(--teal);
    color: var(--paper);
    font-size: 16px;
    line-height: 41px;
    text-align: center;
  }
</style>
</head>
<body>
  <div class="page">
    <svg class="header-wave" width="847" height="120" viewBox="0 0 847 120" aria-hidden="true">
      <path d="M0,0 H847 V48 C720,80 540,78 420,50 C300,22 130,12 0,40 Z" fill="var(--lime)"/>
      <path d="M0,62 C120,24 300,22 430,58 C560,94 740,104 847,58" fill="none" stroke="var(--teal)" stroke-width="7"/>
    </svg>

    <p class="brand-mark">BLP</p>

    <h1 class="content content-title">Lorem ipsum dolor sit amet, consectetur adipiscing elit,</h1>

    <div class="content content-body">
      <p>Sed ut perspiciatis unde omnis iste natus error sit voluptatem accusantium doloremque laudantium, totam rem aperiam, eaque ipsa quae ab illo inventore veritatis et quasi architecto beatae vitae dicta sunt explicabo. Nemo enim ipsam voluptatem quia voluptas sit aspernatur aut odit aut fugit, sed quia consequuntur magni dolores eos qui ratione voluptatem sequi nesciunt.</p>
      <p>Neque porro quisquam est, qui dolorem ipsum quia dolor sit amet, consectetur, adipisci velit, sed quia non numquam eius modi tempora incidunt ut labore et dolore magnam aliquam quaerat voluptatem. Ut enim ad minima veniam, quis nostrum exercitationem ullam corporis suscipit laboriosam, nisi ut aliquid ex ea commodi consequatur? Quis autem vel eum iure reprehenderit qui in ea voluptate velit esse quam nihil molestiae consequatur, vel illum qui dolorem eum fugiat quo voluptas nulla pariatur.</p>
      <p class="spaced">Ut enim ad minima veniam, quis nostrum exercitationem ullam corporis suscipit laboriosam, nisi ut aliquid ex ea commodi consequatur? Quis autem vel eum iure reprehenderit qui in ea voluptate velit esse quam nihil molestiae consequatur, vel illum qui dolorem eum fugiat quo voluptas nulla pariatur</p>
    </div>

    <svg class="footer-bars" width="270" height="36" viewBox="0 0 270 36" aria-hidden="true">
      <polygon points="0,4 190,4 198,13 0,13" fill="var(--lime)"/>
      <polygon points="0,19 246,19 258,32 0,32" fill="var(--teal)"/>
    </svg>

    <p class="footer-name">Bright Ledger Path LLC</p>

    <div class="page-number"><span>1</span></div>
  </div>
</body>
</html>
```